Brindle construction ltd staionary design
Project: Stationary
Stationary - Construction
Stationary
Professional
Directors Dan Brindle / Mark Brindle
BRINDLE CONSTRUCTION (GLOUCESTER) LTD
14 wexcombe road Gloucester GL4 8RQ
Brindleconstructionltd@fernmail.example
www.brindleconstructionlimited.example
would like stationary pack designed: business card, letterhead, envelope ect. Also a site sign please. Business card i would like black background to contrast my green logo with the logo in middle and details underneath. Letterhead i will leave to designer to come up with options. On site sign can i have logo ontop as main feature and underneath contact info with services incl ( New Builds, Extensions, Conversions, Refurbishments, Groundworks, Block Paving.) In logo attached use main logo ontop.
Main logo and underneath building contractor & Block paving specialist

```html
<!DOCTYPE html>
<html lang="en">
<head>
<meta charset="utf-8">
<title>Brindle Construction Ltd – Business Cards</title>
<link rel="stylesheet" href="https://fonts.googleapis.com/css2?family=Arimo:wght@400;700&display=swap">
<style>
  :root {
    --bg: #e9e4de;
    --card-white: #ffffff;
    --green-dark: #0d5a2c;
    --green-mid: #1a7a3c;
    --green-light: #2f9a4e;
    --ink: #3a3a3a;
    --rule: #8a8a8a;
    --white: #ffffff;
  }
  * { box-sizing: border-box; margin: 0; padding: 0; }
  html, body { width: 1200px; height: 714px; overflow: hidden; }
  body {
    background: var(--bg);
    font-family: "Arimo", Arial, sans-serif;
    position: relative;
  }
  .card {
    position: absolute;
    border-radius: 14px;
    overflow: hidden;
    box-shadow: 0 6px 18px rgba(0,0,0,0.18);
  }
  .card--front { left: 91px; top: 120px; width: 466px; height: 262px; background: var(--card-white); }
  .card--back-green {
    left: 595px; top: 65px; width: 463px; height: 266px;
    background: linear-gradient(90deg, var(--green-dark) 0%, var(--green-mid) 60%, var(--green-light) 100%);
    display: flex; align-items: center; justify-content: center;
  }
  .card--back-white {
    left: 355px; top: 372px; width: 463px; height: 264px; background: var(--card-white);
    display: flex; align-items: center; justify-content: center;
  }
  .swoosh { position: absolute; left: 0; top: 0; width: 100%; height: 100%; }
  .director {
    position: absolute; right: 24px; top: 20px; text-align: right; color: var(--white);
  }
  .director__name { font-size: 14px; font-weight: 700; }
  .director__company { font-size: 9px; margin-top: 4px; }
  .wordmark {
    font-weight: 700;
    text-transform: uppercase;
    line-height: 1;
    text-align: center;
  }
  .wordmark__name { display: block; letter-spacing: 1px; }
  .wordmark__sub { display: block; letter-spacing: 3px; }
  .wordmark--front { position: absolute; left: 30px; top: 124px; color: var(--green-mid); }
  .wordmark--front .wordmark__name { font-size: 40px; }
  .wordmark--front .wordmark__sub { font-size: 11px; margin-top: 3px; }
  .wordmark--white { color: var(--white); }
  .wordmark--green { color: var(--green-mid); }
  .wordmark--white .wordmark__name, .wordmark--green .wordmark__name { font-size: 48px; }
  .wordmark--white .wordmark__sub, .wordmark--green .wordmark__sub { font-size: 14px; margin-top: 4px; }
  .details {
    position: absolute; left: 32px; top: 200px;
    display: flex; font-size: 9px; color: var(--ink); line-height: 14px;
  }
  .details__address { width: 76px; border-right: 1px solid var(--rule); }
  .details__contact { padding-left: 12px; }
</style>
</head>
<body>
  <article class="card card--front" aria-label="Business card front">
    <svg class="swoosh" viewBox="0 0 466 262" preserveAspectRatio="none" aria-hidden="true">
      <defs>
        <linearGradient id="greenBand" x1="0" x2="1" y1="0" y2="0">
          <stop offset="0" stop-color="#0d5a2c"/>
          <stop offset="1" stop-color="#2f9a4e"/>
        </linearGradient>
        <linearGradient id="greyBand" x1="0" x2="1" y1="0" y2="0">
          <stop offset="0" stop-color="#eeeff0"/>
          <stop offset="1" stop-color="#a3a6a8"/>
        </linearGradient>
      </defs>
      <path d="M0 60 C160 38 340 52 466 104 V128 C340 78 160 68 0 82 Z" fill="url(#greyBand)"/>
      <path d="M0 0 H466 V96 C340 44 160 30 0 54 Z" fill="url(#greenBand)"/>
    </svg>
    <div class="director">
      <p class="director__name">Directors Dan Brindle</p>
      <p class="director__company">Brindle Construction (Gloucester) LTD</p>
    </div>
    <h1 class="wordmark wordmark--front">
      <span class="wordmark__name">Brindle</span>
      <span class="wordmark__sub">Construction Ltd</span>
    </h1>
    <div class="details">
      <div class="details__address">
        <p>14 wexcombe road</p>
        <p>Gloucester, GL4 8RQ</p>
      </div>
      <div class="details__contact">
        <p>P: 01452 000471 &nbsp;|&nbsp; C: 07700 900318</p>
        <p>Brindleconstructionltd@fernmail.example</p>
        <p>www.brindleconstructionlimited.example</p>
      </div>
    </div>
  </article>

  <article class="card card--back-green" aria-label="Business card back, green">
    <p class="wordmark wordmark--white">
      <span class="wordmark__name">Brindle</span>
      <span class="wordmark__sub">Construction Ltd</span>
    </p>
  </article>

  <article class="card card--back-white" aria-label="Business card back, white">
    <p class="wordmark wordmark--green">
      <span class="wordmark__name">Brindle</span>
      <span class="wordmark__sub">Construction Ltd</span>
    </p>
  </article>
</body>
</html>
```